MENU DESIGN FOR KESARI LOOM RESTUARNT

1.NEED TRI FOLD MENU FOR TAKE OUT FRONT AND BACK JUST LIKE I HAVE ATTACHED THE MENU .....IT COULD EVEN ALMOST IDENTICAL. ( COPY THE MENU ITEMS AT THE BOTTOM OF THIS PAGE.

2. I NEED A POSTER FOR LUNCH COMBO 11AM-2PM
THRE ARE 3 COMBOS
A....HIT_____ SERVED WITH RICE AND ONE ENTREE WITH PCS OF FRESH TANDOORI NAAN BREAD IN 7" CONTAINER....13

B...SUPERHIT......SERVED WITH RICE, SALAD.NAAN, POP, AND ONE ENTREE .....$15

C...BLOCKBUSTER.....SERVED WITH RICE, SALAD, NAAN, POP, AND ONE ENTEE AND ONE ADD-ON....$18

BOTTOM OF THE PAGE PLEASE WE WILL HAVE LIST OF ENTEE + ADD WITH PRICE ...PLS NOTE WE WILL HAVE 10 ENTREE WHIS WILL ALSO TRANSLATE TO 10 ADD ON

AFTER THE DESIGN YOU CAN ATTACH THIS POSTER TO TAKEOUNT MENU WHICH WILL TAKE 1 PAGE.

HER IS THE TAKE OUT MENU ITEMS IN SECTIONS

TANDOORI DINNERS for meat lovers….
Served with rice, salad, roti or naan.

"Signature" BONELESS CHICKEN TIKKA ……………………………
-appetizer $10 / single dinner $15/ big dinner $20
boneless diced chicken marinated with KL secret masala and cooked in tandoor.

"Haryali" BONELESS CHICKEN TIKKA ……………………………………
10/15/20
boneless dice chicken marinated with mint and cilantro cooked in tandoor

"Malai" BONELESS CHICKEN TIKKA…………………………………………………………………
10/15/20
boneless diced chicken marinated with cheese, yogurt and mild spices and cooked in tandoor

"Hot n Spicy" BONELESS CHICKEN TIKKA……………………………………………………………………….
12/17/25
boneless dice chicken marinated with hot spices and cooked in tandoor.

CHICKEN SEEKH KABOB…………………………………………………………………10/15/20

minced ground chicken cooked in tandoor

TANDOORI CHICKEN bone-in……………………………………………………………………………10/15/20
chicken pcs marinated in seasoning and cooked in tandoor.……………………

TANDOORI CHICKEN LEGS

8/10/18

marinated chicken legs cooked in tandoor

TANDOORI CHICKEN WINGS

8/10/18

marinated chicken wings cooked in the tandoor

LAMB CHOPS KABOB……………………………………………………………………

18/22/32

marinated lamb chops in blended spices cooked in tandoor.

SHOULDER LAMB CHOP KEBOB

15/20/30

FISH TIKKA ………………………………………………………………………………………………15/20/32

Moist & tender spice marinated chunks of Salmon cooke in tandoor

TANDOOR SHRIMP………………………………………………………………

17/20/35

marinated shrimp cooked in tandoor.

TANDOORI PANEER TIKKA

10/15/20

chanks of paneer marinated in spices cooked in a tandoor

TANDOORI VEG. KEBOBS

10/15/20

marinated fresh vegetables cooked in a tandoor

**********+++++++=====

—————————TANDOORI KEBOB PLATERS————————————————

4 PERSON $32 6 PERSON $42 8 PERSON $50

———————————TANDOORI WRAPS———————————————————

CHICKEN TIKKA KEBOB WRAP $10
CHICKEN SEEKH KEBOB WRAPS $10
“HOT & SPICY” CHICKEN TIKKA WRAP $12
SALMON FISH TIKKA WRAP
PANEER TIKKA WRAP

VEGETARIAN MAIN COURSE CURRIES SMALL MEDIUM LARGE

CHANNA MASALA $6 $10 $15

DAAL MAKHANI 8 12 17

PANEER MAKHANI 8 12 17

KARAHI PANEER 8 12 17

PALAK PANEER 8 12 17

CHILLIE PANEER 9 13 18

BENGAN AFGHANI 9 12 17

BENGAN BHARTHA 8 12 17

MIX VEG. 8 12 17

VEG. MANCHURIAN 10 14 18

==========SIDES========
TAWA ROTI $1.50
TANDOORI ROTI $1.75
TANDOORI BUTTER NAAN $2
TANDOORI PLAIN NAAN $1.75
TANDOORI GARLIC NAAN $2.50
PLAIN PARATHA $2.50
TAWA NAAN $3.00
BATURA $1.50

BASMATI RICE SMALL $3.50SM LARGE $5
SALAD $3.50
SALAD UPGRADE $4.75
MASALA FRIES
RAITA $3.50

=============== PLATER / ROLL 12PM-4PM =============

2 VEG. CURRY+NAAN+RICE $10
1 VEG. CURRY+NAAN+RICE $8.50
VEG. CURRY ON RICE $7.50

CHANNA / KADAI PANEER / PALAK PANEER / PALAK PANEER / MIX VEG. $8

MEAT LOVERS MAIN COURSE CURRIES

BONELESS BUTTER CHICKEN……………………………………………………………
S $11 ……M15…….L24
diced boneless tandoori chicken cooked in butter and creamy sauce.

KADAI CHICKEN MASALA…………………………………………………………………
S$11……..M$15……..L24
boneless chicken cooked in spices and thick gravy.

CHICKEN TIKKA MASALA………………………………………………………………………………11/15/24
tandoori chicken tikka cooked with spice and gravy.

CHICKEN KOFTA CURRY………………………………………………………………………………11/15/24
chicken kofta cooked in tomatoes and spices.

AFGHANI CHICKEN HARYALI…………………………………………………………………………………11/15/24
chicken cooked with spinach and spices.

CHICKEN VINDALOO……………………………………………………………………………
12/18/29
boneless chicken cooked with potatoes & spices in a thick gravy.

CHICKEN CURRY…..

11/15/24

boneless chicken cooked in the soup gravy

CHILLIE CHICKEN WITHG RAVY

12/18/29

METHI MALAI CHICKEN

11/15/24

boneless chicken cooked cheese and methi

LAMB VINDALOO……………………………………………………………………

13/20/29

boneless lamb cooked with potatoes & spices in a thick gravy.

AFGHANI HARYALI LAMB………………………………………………………………………
13/20/29
lamb cooked with spinach and spices.

SHRIMP VINDALOO……………………………………………………………………
13/20/29
shrimp cooked in the thick spicy sauce.

TANDOORI SHRIMP MASALA

15/25/32

FISH TIKKA MASALA…………………………………………………………………………

15/20/32

fish in spicy curry sauce.

SPECIAL MEALS

LAMB BIRYANI……………………………………………………………………………………………………………..$10

lamb seasoned with fragrant spices and fresh herbs.

CHICKEN BIRYANI…………………………………………………………………………………………………………$9
chicken seasoned with fragrant spices and fresh herbs cooked with rice.

check out our website www.kesariloom.ca FOR

SPCIALS DAILY
SPECIAL ORDERS MENU
DESSRT MENU
DRINK MENU
DESSERT MENU

BENGAN BHARTA
comprises bhurtha (minced vegetables) made from eggplant (baingan) which is grilled over charcoal or direct fire, to infuse the dish with a smoky flavour

PANEER MAKHANI
COTTAGE CHEESE COOKED WITH BUTTER AND CREAMY SAUCE.

VEG. MANCHURIAN AND CHILLIE PANEER- PLS KEEP AT THE SAME PLACE

PLS KEEP VEG SNACKS WITH PRICE CHANGE

ALL VEG SAME WITH PRICE

Target Market(s)

PEOPLE WHO LOVE FRESH INDIAN FOOD

Font styles to use
Decorative
Script

Colors
ec1f27
fdf1e7
f68e4e
fbed22
ffcf3e
faa54b
f68d4c
e34197

Requirements
Must have
• LOGO
• SIZES
• PRICE
• SOME VISUAL
• FILM OR MOVIE THEME
• ACTOR DIRECTOR CINEMA FEEL
Nice to have
• CURRY COMBOS IN FILM REEL NICE TO HAVE BUT NOT A MUS AS I M LOOKING FOR MORE ELEGANT DESIGN NOT A CARTOONI OR BUSY
• MUST BE PROFESSIONAL LOOK
• SIMPLE
• EASY
• ATTRACTIVE

```html
<!DOCTYPE html>
<html lang="en">
<head>
<meta charset="utf-8">
<title>Kesari Loom – Lunch Take-Out Combos</title>
<link rel="stylesheet" href="https://fonts.googleapis.com/css2?family=Arimo:wght@700&family=Fredoka:wght@600&display=swap">
<style>
  :root{
    --red:#ec1f27;
    --cream:#fdf1e7;
    --orange:#f68e4e;
    --yellow:#fbed22;
    --gold:#ffcf3e;
    --amber:#faa54b;
    --magenta:#e34197;
    --berry:#c9196e;
    --plum:#7a1f6b;
    --white:#ffffff;
  }
  *{margin:0;padding:0;box-sizing:border-box}
  html,body{width:943px;height:1200px;overflow:hidden;background:var(--white)}
  .poster{
    position:relative;width:943px;height:1200px;overflow:hidden;
    background:linear-gradient(160deg,#b81a74 0%,var(--berry) 40%,#e1466b 62%,var(--orange) 80%,var(--amber) 100%);
    font-family:"Arimo",Arial,sans-serif;color:var(--white);
  }
  .hero-scene{
    position:absolute;left:0;top:0;width:943px;height:660px;
    background:
      radial-gradient(ellipse at 20% 30%,rgba(246,142,78,.75),transparent 45%),
      radial-gradient(ellipse at 80% 25%,rgba(227,65,151,.8),transparent 50%),
      radial-gradient(ellipse at 55% 55%,rgba(255,207,62,.45),transparent 45%),
      linear-gradient(180deg,#5a2a7a 0%,#a63a8a 40%,#d23c8c 75%,rgba(201,25,110,0) 100%);
  }
  .brand-seal{
    position:absolute;left:379px;top:20px;width:202px;height:202px;border-radius:50%;
    background:var(--white);border:9px solid var(--red);
    display:flex;align-items:center;justify-content:center;
    box-shadow:0 4px 14px rgba(0,0,0,.35);
  }
  .brand-name{font-family:"Arimo",Arial,sans-serif;font-weight:700;font-size:22px;color:var(--red);letter-spacing:1px}
  .ribbon{position:absolute;left:125px;top:232px;width:715px;height:118px}
  .ribbon-text{
    position:absolute;left:150px;top:282px;width:570px;text-align:center;
    font-family:"Fredoka",sans-serif;font-weight:600;font-size:35px;letter-spacing:1px;
    text-shadow:0 2px 4px rgba(0,0,0,.45);
  }
  .combo-photo{
    position:absolute;left:47px;width:360px;border-radius:6px;
    border:4px solid var(--plum);box-shadow:0 3px 10px rgba(0,0,0,.4);
  }
  .photo-hit{top:398px;height:241px;background:linear-gradient(135deg,#f3ece2 0%,#e9d9b8 45%,#f0c63a 70%,#b0522a 100%)}
  .photo-super{top:652px;height:244px;background:linear-gradient(135deg,#e9c9a0 0%,#f2f0ea 40%,#8fbf5a 60%,#d46a2a 85%,#f3f1ee 100%)}
  .photo-block{top:910px;height:278px;background:linear-gradient(135deg,#f4d45a 0%,#c3632a 40%,#9b3a18 70%,#e8b050 100%)}
  .price-badge{
    position:absolute;width:98px;height:98px;border-radius:50%;
    background:var(--white);box-shadow:0 3px 8px rgba(0,0,0,.4);
    display:flex;align-items:center;justify-content:center;
  }
  .price-badge span{
    width:82px;height:82px;border-radius:50%;display:flex;align-items:center;justify-content:center;
    font-family:"Arimo",Arial,sans-serif;font-size:31px;font-weight:700;color:var(--white);
  }
  .badge-hit{left:20px;top:390px}.badge-hit span{background:radial-gradient(circle at 35% 30%,#f04a3a,#b8121a)}
  .badge-super{left:13px;top:655px}.badge-super span{background:radial-gradient(circle at 35% 30%,#a2398f,#5e1760)}
  .badge-block{left:15px;top:903px}.badge-block span{background:radial-gradient(circle at 35% 30%,#fbb04a,#e06a1a)}
  .combo-copy{position:absolute;left:440px;text-shadow:0 2px 3px rgba(0,0,0,.35)}
  .combo-title{position:absolute;white-space:nowrap;font-size:31px;font-weight:700}
  .combo-size{position:absolute;white-space:nowrap;font-size:18px;font-weight:700}
  .combo-portion{position:absolute;white-space:nowrap;font-size:25px;font-weight:700}
  .combo-includes{position:absolute;width:420px;font-size:17.5px;font-weight:700;line-height:1.1}
</style>
</head>
<body>
<main class="poster">
  <div class="hero-scene" role="img" aria-label="Colourful film dance scene with performers in sparkling costumes"></div>

  <div class="brand-seal"><span class="brand-name">KESARI LOOM</span></div>

  <svg class="ribbon" viewBox="0 0 715 118" aria-hidden="true">
    <defs>
      <linearGradient id="ribbonFill" x1="0" y1="0" x2="0" y2="1">
        <stop offset="0" stop-color="#f2545a"/>
        <stop offset="1" stop-color="#c8141e"/>
      </linearGradient>
    </defs>
    <path d="M40 8 Q200 -4 360 10 Q520 22 690 6 L692 20 Q540 38 370 26 Q200 14 44 26 Z" fill="#9c0f16"/>
    <path d="M0 20 Q180 4 360 22 Q540 40 715 20 L700 96 Q530 116 360 98 Q190 80 16 100 Z" fill="url(#ribbonFill)"/>
    <path d="M715 20 Q690 40 700 60 L715 52 Z" fill="#a10f17"/>
  </svg>
  <div class="ribbon-text">FOR LUNCH TAKE-OUT ONLY</div>

  <div class="combo-photo photo-hit" role="img" aria-label="Naan, yellow rice and a curry entree"></div>
  <div class="price-badge badge-hit"><span>$13</span></div>
  <div class="combo-copy">
    <div class="combo-title" style="top:408px">LIL ( "HIT")</div>
    <div class="combo-size" style="top:458px">7" CONTAINER</div>
    <div class="combo-portion" style="top:524px">AVERAGE PORTION</div>
    <div class="combo-includes" style="top:593px">INCLUDES RICE,NAAN, ONE ENTREE</div>
  </div>

  <div class="combo-photo photo-super" role="img" aria-label="Curry bowl with rice, naan, salad and raita"></div>
  <div class="price-badge badge-super"><span>$15</span></div>
  <div class="combo-copy">
    <div class="combo-title" style="top:665px">BIG ( "SUPER HIT")</div>
    <div class="combo-size" style="top:716px">8" CONTAINER</div>
    <div class="combo-portion" style="top:788px">AVERAGE PLUS</div>
    <div class="combo-includes" style="top:851px">INCLUDES RICE,NAAN,ONE ENTREE</div>
  </div>

  <div class="combo-photo photo-block" role="img" aria-label="Large plate of spiced chicken curry with rice and naan"></div>
  <div class="price-badge badge-block"><span>$18</span></div>
  <div class="combo-copy">
    <div class="combo-title" style="top:923px">HUGE ('BLOCKBUSTER")</div>
    <div class="combo-size" style="top:978px">9" CONTAINER</div>
    <div class="combo-portion" style="top:1029px">SUPER SIZE PORTION</div>
    <div class="combo-includes" style="top:1072px">INCLUDES RICE, 2 NAAN, SALAS, AND ONE ADD ON OF YOUR CHOICE FROM UPGRADE MENU BELOW OR SIDES</div>
  </div>
</main>
</body>
</html>
```